Letterhead Design Project

We store & repair empty shipping containers owned by the shipping lines.
We have just selected a logo design & now want a business card & letterhead to go with it. (Logo is attached - colours are yellow & dark grey)

ABN: 384 920 17263
ACN: 293 718 406
Address: 218-220 Pellgrove Rd, Marrowdale, 3047
Website: www.tarvelhub.com.au

You will need to make provision for a phone number, fax number & email (which we don't have yet.. so okay to just put in fake ones)

Target Market(s)

Shipping lines, freight forwarders

Industry/Entity Type

Shipping

Requirements
Must have
• Must include the logo attached
Must include our ABN, ACN address as per above

```html
<!DOCTYPE html>
<html lang="en">
<head>
<meta charset="utf-8">
<title>TarvelHub Letterhead</title>
<link rel="stylesheet" href="https://fonts.googleapis.com/css2?family=Overpass:wght@400;500;800&display=swap">
<style>
  :root {
    --slate: #48535c;
    --amber: #fbbd2e;
    --paper: #ffffff;
    --frame: #3e474e;
    --card-edge: #c9cdd1;
  }
  * { margin: 0; padding: 0; box-sizing: border-box; }
  html, body { width: 849px; height: 1200px; overflow: hidden; background: var(--paper); }
  body { font-family: "Overpass", Arial, sans-serif; color: var(--slate); }

  .letterhead {
    position: relative;
    width: 849px;
    height: 1200px;
    background: var(--paper);
    overflow: hidden;
  }
  .letterhead__frame {
    position: absolute;
    inset: 2px 9px 10px 2px;
    border: 1.5px solid var(--frame);
    overflow: hidden;
  }
  .corner { position: absolute; display: block; }
  .corner--top { left: 0; top: 0; width: 380px; height: 260px; }
  .corner--bottom { right: 0; bottom: 0; width: 380px; height: 260px; }

  .brand {
    position: absolute;
    display: flex;
    align-items: center;
    gap: 10px;
    font-weight: 800;
    color: var(--slate);
    letter-spacing: -0.5px;
    line-height: 1;
  }
  .brand__mark { background: var(--amber); flex: none; }
  .brand--header { left: 450px; top: 54px; font-size: 40px; }
  .brand--header .brand__mark { width: 30px; height: 30px; }

  .sender-contact {
    position: absolute;
    left: 66px;
    top: 1096px;
    font-size: 14px;
    line-height: 18.5px;
    color: var(--slate);
    list-style: none;
  }
  .footer-address {
    position: absolute;
    left: 548px;
    top: 1116px;
    color: var(--amber);
    font-weight: 500;
  }
  .footer-address__street { font-size: 11.5px; }
  .footer-address__web { font-size: 16px; margin-top: 3px; letter-spacing: 0.2px; }

  /* Business card */
  .business-card {
    position: absolute;
    left: 220px;
    top: 441px;
    width: 360px;
    height: 242px;
    background: var(--paper);
    border: 1px solid var(--card-edge);
    overflow: hidden;
  }
  .business-card__shape { position: absolute; inset: 0; width: 100%; height: 100%; }
  .brand--card { left: 16px; top: 26px; font-size: 22px; gap: 6px; }
  .brand--card .brand__mark { width: 16px; height: 16px; }
  .business-card__ids {
    position: absolute;
    left: 16px;
    top: 78px;
    font-size: 9.5px;
    line-height: 13px;
    color: var(--slate);
  }
  .business-card__contact {
    position: absolute;
    left: 94px;
    top: 160px;
    font-size: 9.5px;
    line-height: 13.5px;
    color: var(--amber);
    font-weight: 500;
  }
  .business-card__contact .indent { padding-left: 52px; }
  .business-card__contact .label { padding-left: 53px; }
</style>
</head>
<body>
<main class="letterhead">
  <div class="letterhead__frame">
    <svg class="corner corner--top" viewBox="0 0 380 260" role="img" aria-label="Slate corner band in the brand colours">
      <polygon fill="var(--slate)" points="0,0 370,0 0,255"/>
    </svg>

    <svg class="corner corner--bottom" viewBox="0 0 380 260" role="img" aria-label="Slate corner band in the brand colours">
      <polygon fill="var(--slate)" points="10,260 90,140 380,0 380,260"/>
    </svg>

    <div class="brand brand--header">
      <span class="brand__mark"></span>
      <span class="brand__name">TarvelHub</span>
    </div>

    <section class="business-card" aria-label="Business card">
      <svg class="business-card__shape" viewBox="0 0 360 242" preserveAspectRatio="none" role="img" aria-label="Slate band in the brand colours">
        <polygon fill="var(--slate)" points="0,242 70,130 360,0 360,242"/>
      </svg>
      <div class="brand brand--card">
        <span class="brand__mark"></span>
        <span class="brand__name">TarvelHub</span>
      </div>
      <div class="business-card__ids">
        <p>ABN: 384 920 17263</p>
        <p>ACN: 293 718 406</p>
      </div>
      <div class="business-card__contact">
        <p>Address: 218-220 Pellgrove Rd, Marrowdale, 3047</p>
        <p class="indent">www.tarvelhub.com.au</p>
        <p class="label">Phone:</p>
        <p class="label">Fax:</p>
        <p class="label">E-mail:</p>
      </div>
    </section>

    <ul class="sender-contact">
      <li>Phone:</li>
      <li>Fax:</li>
      <li>E-mail:</li>
    </ul>

    <div class="footer-address">
      <p class="footer-address__street">Address: 218-220 Pellgrove Rd, Marrowdale, 3047</p>
      <p class="footer-address__web">www.tarvelhub.com.au</p>
    </div>
  </div>
</main>
</body>
</html>
```